PROMOTION CARD for NEW APPLICATION LAUNCH

Hi need double sided promotion card the size of a postcard.
we car launching a new app, and need to promote
the app is focused on the automotive
the functions are to help remind customers when there car utilities bills are due.
* registration
*Insurance
*CTP due
*Service
* Warranty

Helps sell your car under the ( "Whats New " Button )
Helps you find a better finance or insurance deal.( Zenqa Portal)

Target Market(s)

All consumers who own a Car all ages both male and female

Industry/Entity Type

Automotive

Font styles to use
Sans Serif

Colors
0293ce
9ccb3b
fffbf0

Requirements
Must have
• clean and professional makes you want to down load the app
Nice to have
• clear description about what the app dose feature and functions
• the application will reminder the customer when the
• *registration due
• * insurance due
• *Finance due
• Kelvra picture
• car or road in background
• *CTP due
• *Service due
• *Warranty Due
• it will also pay a payment function so you can pay,
Should not have
• color brown/ no running writing

```html
<!DOCTYPE html>
<html lang="en">
<head>
<meta charset="utf-8">
<title>Drivnel – App Launch Postcard</title>
<link rel="stylesheet" href="https://fonts.googleapis.com/css2?family=Mulish:wght@400;600;700;800&display=swap">
<style>
  :root {
    --blue: #0293ce;
    --green: #9ccb3b;
    --cream: #fffbf0;
    --ink: #111418;
    --ink-soft: #2a2f33;
    --stage: #e4e4e4;
    --phone: #111111;
    --panel: rgba(255, 255, 255, 0.82);
  }
  * { box-sizing: border-box; margin: 0; padding: 0; }
  html, body { width: 1200px; height: 1000px; overflow: hidden; }
  body {
    background: var(--stage);
    font-family: "Mulish", Arial, sans-serif;
    color: var(--ink);
    position: relative;
  }

  /* ---------- Front of card ---------- */
  .card-front {
    position: absolute; left: 118px; top: 34px;
    width: 692px; height: 448px; overflow: hidden;
  }
  .street-photo {
    position: absolute; inset: 0;
    background: linear-gradient(120deg, #d8dadd 0%, #b9bcc2 35%, #8a8fa8 55%, #c9cbd0 75%, #e2e3e5 100%);
  }
  .phone {
    position: absolute; left: 54px; top: 32px; width: 218px; height: 384px;
    background: var(--phone); border-radius: 24px;
    border: 3px solid #555;
  }
  .phone-screen {
    position: absolute; left: 5px; top: 26px; width: 203px; height: 308px;
    background: #fff; text-align: center;
  }
  .phone-brand-mark {
    width: 96px; height: 96px; margin: 26px auto 0;
    background: var(--blue);
  }
  .phone-brand {
    font-size: 34px; font-weight: 700; color: var(--ink); margin-top: 10px;
    letter-spacing: 0.5px;
  }
  .phone-tagline {
    font-size: 14px; font-weight: 800; line-height: 18px; margin-top: 30px;
  }
  .phone-home {
    position: absolute; left: 50%; bottom: 8px; transform: translateX(-50%);
    width: 34px; height: 34px; border-radius: 50%; border: 2px solid #444;
  }
  .reminder-panel {
    position: absolute; left: 294px; top: 34px; width: 346px; height: 382px;
    background: var(--panel); border-radius: 16px;
  }
  .panel-title {
    position: absolute; left: 10px; top: 36px;
    font-size: 23px; font-weight: 700; white-space: nowrap;
  }
  .due-list { position: absolute; list-style: none; font-size: 14px; color: var(--ink-soft); }
  .due-list li { display: flex; align-items: center; height: 16px; margin-bottom: 20px; }
  .due-list li::before {
    content: ""; width: 13px; height: 13px; border-radius: 50%; margin-right: 12px;
    background: var(--dot);
  }
  .due-list.left { left: 16px; top: 104px; --dot: var(--blue); }
  .due-list.right { left: 190px; top: 103px; --dot: var(--green); }
  .due-list li:nth-child(3) { margin-top: -2px; }
  .pill {
    position: absolute; height: 31px; border-radius: 5px;
    color: #fff; font-size: 16px; text-align: center; line-height: 31px;
  }
  .pill.blue { background: var(--blue); }
  .pill.green { background: var(--green); }
  .pill-portal { left: 14px; top: 235px; width: 142px; }
  .pill-news { left: 181px; top: 235px; width: 142px; }
  .pill-pay { left: 14px; top: 310px; width: 142px; height: 26px; line-height: 26px; }
  .pill-note { position: absolute; font-size: 13.5px; color: var(--ink-soft); line-height: 19px; }
  .note-portal { left: 23px; top: 282px; }
  .note-news { left: 181px; top: 283px; width: 160px; }

  /* ---------- Back of card ---------- */
  .card-back {
    position: absolute; left: 389px; top: 498px;
    width: 703px; height: 447px; background: var(--green);
  }
  .feature-button {
    position: absolute; left: 42px; width: 260px; height: 54px; border-radius: 8px;
    background: linear-gradient(90deg, var(--green) 0%, #3fae8a 55%, var(--blue) 100%);
  }
  .feature-button .label {
    position: absolute; left: 0; width: 190px; top: 0; line-height: 54px;
    text-align: center; font-size: 19px; font-weight: 800; color: var(--ink);
  }
  .feature-button .brand-chip {
    position: absolute; right: 14px; top: 7px; width: 48px; height: 40px;
    background: var(--blue); color: #fff; font-size: 10px; font-weight: 700;
    text-align: center; line-height: 62px;
  }
  .btn-portal { top: 36px; }
  .btn-news { top: 220px; }
  .feature-copy {
    position: absolute; left: 44px; width: 266px;
    font-size: 13.6px; line-height: 19.5px; color: var(--ink);
  }
  .copy-portal { top: 102px; }
  .copy-news { top: 286px; }
  .feature-copy b { font-weight: 800; }
  .hotline { position: absolute; left: 41px; top: 392px; font-size: 16.5px; color: var(--ink); }
  .divider { position: absolute; left: 333px; top: 37px; width: 1.5px; height: 372px; background: var(--blue); }
  .info-col { position: absolute; left: 357px; width: 320px; font-size: 14px; line-height: 19.5px; color: var(--ink); }
  .info-heading { font-size: 16px; font-weight: 800; }
  .availability { top: 37px; }
  .intro { top: 77px; }
  .features { top: 154px; }
  .features p + p { margin-top: 19.5px; }
  .download-button {
    position: absolute; left: 359px; top: 329px; width: 284px; height: 54px; border-radius: 10px;
    background: linear-gradient(90deg, var(--cream) -20%, #57b6a6 40%, var(--blue) 100%);
    text-align: center; line-height: 54px;
    font-size: 27px; font-weight: 800; color: var(--green);
  }
  .web { position: absolute; left: 361px; top: 392px; font-size: 16.5px; color: var(--ink); }
</style>
</head>
<body>

<section class="card-front">
  <div class="street-photo" role="img" aria-label="Blurred city street with a blue sports car parked at the kerb"></div>

  <div class="phone" aria-label="Kelvra smartphone">
    <div class="phone-screen">
      <div class="phone-brand-mark"></div>
      <div class="phone-brand">Drivnel</div>
      <p class="phone-tagline">We remember<br>what<br>You forget!</p>
    </div>
    <div class="phone-home"></div>
  </div>

  <div class="reminder-panel">
    <h1 class="panel-title">An app that will remind you</h1>
    <ul class="due-list left">
      <li>Registration Due</li>
      <li>Insurance Due</li>
      <li>Finance Due</li>
    </ul>
    <ul class="due-list right">
      <li>CTP Due</li>
      <li>Service Due</li>
      <li>Warranty Due</li>
    </ul>
    <div class="pill blue pill-portal">Zenqa Portal</div>
    <div class="pill green pill-news">What’s New</div>
    <p class="pill-note note-portal">Helps sell your car</p>
    <div class="pill blue pill-pay">Pay</div>
    <p class="pill-note note-news">Helps you find a better finance or insurance deal.</p>
  </div>
</section>

<section class="card-back">
  <div class="feature-button btn-portal">
    <span class="label">Zenqa Portal</span>
    <span class="brand-chip">drivnel</span>
  </div>
  <p class="feature-copy copy-portal">“<b>Zenqa Portal</b>” button helps customers find a more competitive deal, insurance or finance, or car provide a valuation.</p>

  <div class="feature-button btn-news">
    <span class="label">What’s New</span>
    <span class="brand-chip">drivnel</span>
  </div>
  <p class="feature-copy copy-news">“<b>What’s New</b>” button allows customers to buy and sell automotive products, sush as car parts or sell their cars or see new promotion owners with auto traders.</p>

  <p class="hotline">1300 555 014 and 1300 5 drivnel</p>

  <div class="divider"></div>

  <h2 class="info-col info-heading availability">Available to all Smart phone users</h2>
  <p class="info-col intro">Drivnel app is a collection of online services to enhance your owenership of a motor vehicle.</p>
  <div class="info-col features">
    <p><span class="info-heading">Drivnel Features:</span><br>Vehicle Data and receipt box storage</p>
    <p>Contact details for all vehicle contracts Registration, Insurance, Car ServiceCTP, Warrenty, Roadside, Tolls &amp; fires, Calendar reminders, with direct Payments options for your vehicle utility bills, much more.</p>
  </div>

  <div class="download-button">Free Download</div>
  <p class="web">www.drivnel.net.au</p>
</section>

</body>
</html>
```